Group fitness classes - DL flyer

We need a flyer design for our boutique fitness studio.

We would prefer to see the use of pictures in the design.

One sided. Please allow space around the edges for bleed.

Flyer should have the following text:

Quillmere Ember Studio
Group fitness special – two weeks unlimited group fitness classes for $29*
Enjoy unlimited access to our fantastic group classes including Kinetrix, Yoga, Strength Circuit and Self Defence Martial Arts.
Purchase your pass through our online store by selecting the "Special Offers" option.
Bring this flyer to your first class and receive an extra two weeks free!

www.quillmereemberstudio.com.au
or phone
0412 *** ***
2/41 Corrabin Lane Flemington

*New clients only

Boutique

Serif
Sans Serif

• Photos
• Cartoons

```html
<!DOCTYPE html>
<html lang="en">
<head>
<meta charset="utf-8">
<title>Quillmere Ember Studio – Group Fitness Special Flyer</title>
<link rel="stylesheet" href="https://fonts.googleapis.com/css2?family=Questrial&family=Roboto+Slab:wght@700;900&family=Didact+Gothic&display=swap">
<style>
  :root {
    --stage: #e6e6e6;
    --paper: #ffffff;
    --purple-deep: #3d1f5c;
    --purple: #5a2d82;
    --purple-light: #7a4aa3;
    --orange: #f05a1a;
    --orange-deep: #d93d0c;
    --orange-light: #f7862e;
    --photo-warm: #d9c3b4;
    --photo-cool: #a99aa8;
    --footer: #0c0c0c;
    --white: #ffffff;
  }
  * { margin: 0; padding: 0; box-sizing: border-box; }
  html, body {
    width: 1200px; height: 758px; overflow: hidden;
    background: var(--stage);
  }
  .flyer {
    position: absolute; left: 366px; top: 48px;
    width: 468px; height: 662px;
    background: var(--paper);
    overflow: hidden;
    box-shadow: 0 4px 14px rgba(0,0,0,0.25);
    font-family: "Questrial", "Didact Gothic", sans-serif;
    color: var(--white);
  }
  .flyer-art { position: absolute; inset: 0; }
  .brand {
    position: absolute; left: 10px; top: 16px;
    font-family: "Questrial", sans-serif;
    color: var(--purple); font-size: 15px; line-height: 17px;
    letter-spacing: 1px; text-transform: uppercase;
    display: flex; align-items: center; gap: 7px;
  }
  .brand-dot {
    width: 14px; height: 14px; border-radius: 50%;
    background: var(--purple); flex: none;
  }
  .offer {
    position: absolute; left: 21px; top: 115px;
    width: 200px; height: 200px; text-align: center;
    font-family: "Roboto Slab", serif;
  }
  .offer-title { margin-top: 40px; font-size: 15px; line-height: 18px; font-weight: 700; text-transform: uppercase; }
  .offer-price { font-size: 64px; line-height: 62px; font-weight: 900; letter-spacing: -1px; }
  .offer-note { margin: 6px auto 0; width: 150px; font-size: 8px; line-height: 10px; font-weight: 700; text-transform: uppercase; }
  .intro {
    position: absolute; left: 9px; top: 338px; width: 300px;
    font-size: 15px; line-height: 19px;
  }
  .classes { position: absolute; left: 14px; top: 386px; list-style: none; font-size: 14.5px; line-height: 19.5px; }
  .classes li { display: flex; align-items: center; gap: 6px; }
  .classes svg { width: 9px; height: 9px; flex: none; }
  .how-to {
    position: absolute; left: 10px; top: 474px; width: 360px; text-align: center;
    font-style: italic; font-size: 14.5px; line-height: 18.5px;
  }
  .how-to strong { display: block; font-size: 17.5px; line-height: 24px; font-weight: 700; }
  .web { position: absolute; left: 10px; top: 565px; width: 360px; text-align: center; font-size: 16px; font-weight: 700; }
  .phone { position: absolute; left: 10px; top: 585px; width: 360px; text-align: center; font-size: 27px; font-weight: 700; letter-spacing: 0.5px; }
  .footer {
    position: absolute; left: 0; bottom: 0; width: 468px; height: 40px;
    background: var(--footer); text-align: center;
    font-size: 11px; line-height: 14px; padding-top: 7px;
  }
</style>
</head>
<body>
  <article class="flyer">
    <svg class="flyer-art" width="468" height="662" viewBox="0 0 468 662">
      <defs>
        <linearGradient id="photoTone" x1="0" y1="0" x2="1" y2="1">
          <stop offset="0" stop-color="var(--photo-cool)"/>
          <stop offset="0.5" stop-color="var(--photo-warm)"/>
          <stop offset="1" stop-color="#c7a998"/>
        </linearGradient>
        <linearGradient id="purpleTone" x1="0" y1="0" x2="1" y2="1">
          <stop offset="0" stop-color="var(--purple-light)"/>
          <stop offset="0.5" stop-color="var(--purple)"/>
          <stop offset="1" stop-color="var(--purple-deep)"/>
        </linearGradient>
        <radialGradient id="orangeTone" cx="0.4" cy="0.35" r="0.7">
          <stop offset="0" stop-color="var(--orange-light)"/>
          <stop offset="0.6" stop-color="var(--orange)"/>
          <stop offset="1" stop-color="var(--orange-deep)"/>
        </radialGradient>
      </defs>
      <rect class="class-photo" x="150" y="0" width="318" height="622" fill="url(#photoTone)" role="img" aria-label="Photo of smiling women in a group fitness class lifting purple hand weights"/>
      <path class="purple-sweep" d="M0,162 C70,148 150,128 225,104 C300,250 375,450 425,622 L0,622 Z" fill="url(#purpleTone)"/>
      <circle class="offer-disc" cx="121" cy="215" r="100" fill="url(#orangeTone)"/>
      <rect class="footer-band" x="0" y="622" width="468" height="40" fill="var(--footer)"/>
    </svg>

    <div class="brand"><span class="brand-dot"></span><span>Quillmere Ember<br>Studio</span></div>

    <div class="offer">
      <p class="offer-title">Group<br>Fitness Special</p>
      <p class="offer-price">$29</p>
      <p class="offer-note">Two weeks unlimited group fitness classes</p>
    </div>

    <p class="intro">Enjoy unlimited access to our fantastic group classes including:</p>
    <ul class="classes">
      <li><svg viewBox="0 0 10 10"><path d="M1,5 L4,8 L9,1" fill="none" stroke="var(--white)" stroke-width="1.8"/></svg>Kinetrix</li>
      <li><svg viewBox="0 0 10 10"><path d="M1,5 L4,8 L9,1" fill="none" stroke="var(--white)" stroke-width="1.8"/></svg>Yoga</li>
      <li><svg viewBox="0 0 10 10"><path d="M1,5 L4,8 L9,1" fill="none" stroke="var(--white)" stroke-width="1.8"/></svg>Strength Circuit</li>
      <li><svg viewBox="0 0 10 10"><path d="M1,5 L4,8 L9,1" fill="none" stroke="var(--white)" stroke-width="1.8"/></svg>Self Defence Martial Arts</li>
    </ul>

    <p class="how-to">Purchase your pass through our online store<br>by selecting the "Special Offers" option.<br>Bring this flyer to your first class and receive an<strong>extra two weeks free!</strong></p>

    <p class="web">www.quillmereemberstudio.com.au</p>
    <p class="phone">0412 583 296</p>

    <footer class="footer">Quillmere Ember Studio<br>2/41 Corrabin Lane, Flemington, Melbourne, Vic, 3031</footer>
  </article>
</body>
</html>
```